Velvet Crest Car Detailing Brochure

I would like a trifold brochure designed for my car detailing business. The background has to be full black or mostly black with some designing using only colors present in our logo.

Front page must have our logo and name, list of services, a photo and mybe our phone number but no long text.

Inside I want to present each service one by one with its description and a photo representing/showing each service. (I will provide the text below). For photos, use stock photos and I will add come of mines already too.

On the back of the brochure I want to have contact & info: phone number, opening hours, address, website, Instagram.

Outside left I want the text About us and photo/design.

I want the brochure to be neat, professional, easy to read, but at the same time not too boring.

Text:
1. About us
a. the ultimate destination for car care in Geneva. We provide personalized, detail-oriented services that bring out the best in your car. With our expert techniques and dedicated approach, we ensure that your car receives the utmost care and attention. Experience a place where passion meets precision and let us create an exceptional car care experience designed just for you.
2. Services:

DETAILING & HAND WASH

• Comprehensive exterior & interior care
• Personalisation and tailored cleaning packages
• Decontamination
• Premium products
• Attention to detail for a perfect finish

POLISHING

• Eliminates scratches, holograms
• Revives and protects paint
• Ensures lasting gloss
• Enhances paint life
• Preserves car’s value and beauty

CERAMIC TREATMENT

• Durable paint protection
• Water-repellent (hydrophobic) effect
• Easier cleaning, enhanced shine
• Long-term surface safeguarding
• Shields against environmental impacts

DRY ICE WASH

• Innovative, waterless method
• Safe for all car parts
• Deep cleans, removes odors
• Allergen-free, antibacterial
• Gentle, effective
• Advanced cleaning technology

COVERING

• Personalized vehicle styling
• More than 150 colours available
• Clean cut without using a cutter
• High-quality, durable materials
• Custom designs available

PROTECTION FILM

• Invisible, durable shield
• Self-healing technology
• 10-year warranty by QR VONT

DETAILING BOUTIQUE

• Premium brands available
• Buy on site during your visit
• Marble Harbour, Zeb Autos, DRUP Polaro
• Essential for at-home car care
• Perfect for quick touch-ups
(for these three brands you can put their logos

Target Market(s)

Our target market includes car owners of all price ranges, with a special focus on those who are passionate about their vehicles. We cater to clients who value excellent service and results, and seek to maintain their cars in pristine condition.

Industry/Entity Type

Automobile / Car detailing

Colors

Designer to choose colors to be used in the design.

Requirements
Must have
• Brand Consistency: The brochure must adhere to our brand colors and style, particularly utilizing the colors present in our logo. Trifold Layout: The design must be specifically tailored for a trifold brochure format. Legibility: Text must be easy to read against the mostly black background, with appropriate font size and style. Professional Look and Feel: The overall design must convey professionalism while being engaging and not overly complex. Photo representation: each service description should have a phot presenting it.
Should not have
• Overcrowded Design: Avoid cluttering with too much text or too many images. The layout should be clean and easy to navigate. Cartoonish Fonts or Graphics: Avoid using unprofessional or casual fonts and graphics that do not align with the upscale and professional image of our business. Distracting Backgrounds: The background should complement and not overpower the content. Stick to the theme of mostly black with design elements from our logo.

```html
<!DOCTYPE html>
<html lang="en">
<head>
<meta charset="utf-8">
<title>Velvet Crest Car Detailing – Trifold Brochure</title>
<link rel="stylesheet" href="https://fonts.googleapis.com/css2?family=Montserrat:ital,wght@0,400;0,500;0,700;0,800;1,800&family=Oswald:wght@500&display=swap">
<style>
:root{
  --pink:#d6398f;
  --purple:#8a5cc0;
  --blue:#3f8fd6;
  --ink:#231f22;
  --ink-soft:#2d292c;
  --white:#ffffff;
  --text:#e9e6ea;
  --rule:#5a5559;
  --bg:#ececec;
}
*{box-sizing:border-box;margin:0;padding:0}
html,body{width:1200px;height:1200px;overflow:hidden}
body{background:var(--bg);font-family:"Montserrat",sans-serif;color:var(--text);position:relative}
.spread{position:absolute;left:229px;width:741px;height:571px;background:var(--ink);overflow:hidden;box-shadow:0 4px 14px rgba(0,0,0,.18)}
.spread--outside{top:20px}
.spread--inside{top:609px}
.panel{position:absolute;top:0;width:247px;height:571px;overflow:hidden}
.panel--1{left:0}.panel--2{left:247px}.panel--3{left:494px}
.photo{position:absolute}

/* outside: about */
.about{background:linear-gradient(180deg,var(--pink) 0%,var(--purple) 50%,var(--blue) 100%);position:absolute;left:0;top:0;width:247px;height:369px;text-align:center;padding:0 20px}
.about__title{font-weight:800;font-size:15px;letter-spacing:3px;color:var(--white);margin-top:62px}
.about__text{font-size:12.2px;line-height:18.4px;color:var(--white);margin-top:9px}
.about__photo{left:0;top:369px;width:247px;height:202px;background:linear-gradient(160deg,#9a9a9c 0%,#4a4a4d 55%,#1f1f21 100%)}

/* outside: thanks */
.thanks__photo{left:0;top:0;width:247px;height:571px;background:linear-gradient(180deg,#5a5660 0%,#3a3640 35%,#262228 60%,var(--ink) 80%)}
.badge{position:absolute;left:36px;top:222px;width:66px;height:66px;border-radius:50%;background:linear-gradient(135deg,var(--blue),var(--purple) 45%,var(--pink));color:var(--white);font-weight:800;font-size:15px;line-height:14px;padding:20px 0 0 10px}
.thanks__title{position:absolute;left:0;width:247px;text-align:center;color:var(--white);font-weight:800;top:284px;font-size:38px;letter-spacing:-.5px}
.thanks__sub{position:absolute;left:0;width:247px;text-align:center;color:var(--white);font-weight:800;font-size:20.5px;line-height:30px;top:325px;letter-spacing:.3px}
.rule{position:absolute;height:1px;background:var(--rule)}
.contact{position:absolute;left:45px;top:400px;list-style:none;font-size:7.8px;line-height:10.5px;color:var(--text)}
.contact li{display:flex;gap:12px;align-items:flex-start;margin-bottom:6px}
.contact svg{width:11px;height:11px;flex:none;margin-top:1px}
.call{position:absolute;left:0;width:247px;text-align:center;top:478px;color:var(--pink);font-weight:800;font-size:15px;letter-spacing:3.5px}
.phone{position:absolute;left:0;width:247px;text-align:center;top:502px;color:var(--white);font-family:"Oswald",sans-serif;font-weight:500;font-size:35px;letter-spacing:.5px}

/* outside: front */
.front__mark{position:absolute;left:80px;top:42px;width:88px;height:88px;border-radius:50%;border:3px solid var(--pink)}
.front__name{position:absolute;left:0;width:247px;text-align:center;top:138px;font-size:18px;line-height:22px;font-weight:400;color:var(--white);letter-spacing:.5px}
.band{position:absolute;left:0;top:0;width:247px;height:571px}
.front__car{left:6px;top:212px;width:234px;height:130px;border-radius:40px 50px 18px 18px;background:linear-gradient(180deg,#3b8ccf 0%,#1f5e98 60%,#1b1b1e 100%)}
.services__title{position:absolute;left:0;width:247px;text-align:center;top:380px;color:var(--pink);font-weight:800;font-size:16px;letter-spacing:3px}
.services__list{position:absolute;left:48px;width:160px;top:404px;list-style:none}
.services__list li{font-size:12.4px;line-height:18.2px;text-align:center;color:var(--text);border-bottom:1px solid var(--rule);white-space:nowrap;letter-spacing:.2px}
.services__list li:first-child{border-bottom:1px solid var(--rule)}
.services__list li:last-child{border-bottom:none}
.services__list{left:44px;width:162px}
.services__list li{margin-left:-10px;margin-right:-6px}

/* inside */
.service__title{color:var(--pink);font-weight:800;font-style:italic;font-size:13px;letter-spacing:.2px}
.bullets{list-style:none;margin-top:5px}
.bullets li{position:relative;padding-left:10px;font-size:9.5px;line-height:11.7px;color:var(--text)}
.bullets li::before{content:"";position:absolute;left:0;top:4px;width:4px;height:4px;background:var(--purple)}
.service{position:absolute}
.thumb{position:absolute;width:52px;height:86px;border-left:2px solid var(--blue);border-bottom:2px solid var(--pink)}
.wash__photo{left:0;top:0;width:247px;height:362px;clip-path:polygon(0 0,100% 0,100% 77%,0 100%);background:linear-gradient(150deg,#c9c9cc 0%,#6e6e72 40%,#2a2a2d 80%)}
.wash{left:18px;top:384px;width:220px}
.wash .service__title{font-size:15px;line-height:19px}
.wash .bullets li{font-size:12.4px;line-height:14.6px;padding-left:17px;margin-bottom:1.5px}
.wash .bullets li::before{top:5px;width:5px;height:5px}
.inside__car{left:30px;top:370px;width:162px;height:120px;border-radius:30px 30px 14px 14px;background:linear-gradient(180deg,#b3253a 0%,#7a1424 60%,#2a1a1d 100%)}
</style>
</head>
<body>

<section class="spread spread--outside" aria-label="Brochure outside">
  <div class="panel panel--1">
    <div class="about">
      <h2 class="about__title">ABOUT US</h2>
      <p class="about__text">the ultimate destination for car care in Geneva. We provide personalized, detail-oriented services that bring out the best in your car. With our expert techniques and dedicated approach, we ensure that your car receives the utmost care and attention. Experience a place where passion meets precision and let us create an exceptional car care experience designed just for you.</p>
    </div>
    <div class="photo about__photo" role="img" aria-label="Silver SUV above a dark car covered in foam during a hand wash"></div>
  </div>

  <div class="panel panel--2">
    <div class="photo thanks__photo" role="img" aria-label="Hand holding a rotary polisher with a blue pad against a dark car body"></div>
    <div class="badge">24/7<br>OPEN</div>
    <h2 class="thanks__title">THANKS</h2>
    <p class="thanks__sub">FOR SELECT<br>OUR SERVICES</p>
    <div class="rule" style="left:46px;width:160px;top:392px"></div>
    <ul class="contact">
      <li><svg viewBox="0 0 12 12" fill="none" stroke="#d6398f" stroke-width="1.2"><path d="M6 11s4-3.8 4-6.5a4 4 0 0 0-8 0C2 7.2 6 11 6 11z"/><circle cx="6" cy="4.6" r="1.4"/></svg><span>You address will come here<br>street, city, location</span></li>
      <li><svg viewBox="0 0 12 12"><rect x="1" y="2.5" width="10" height="7" rx="1" fill="#d6398f"/><path d="M1.5 3l4.5 3.5L10.5 3" fill="none" stroke="#231f22" stroke-width="1"/></svg><span>hello@velvetcrest.example</span></li>
      <li><svg viewBox="0 0 12 12" fill="none" stroke="#d6398f" stroke-width="1"><circle cx="6" cy="6" r="4.8"/><ellipse cx="6" cy="6" rx="2" ry="4.8"/><path d="M1.2 6h9.6"/></svg><span>velvetcrest.example</span></li>
    </ul>
    <div class="rule" style="left:46px;width:160px;top:466px"></div>
    <p class="call">CALL NOW</p>
    <p class="phone">555 014 2287</p>
  </div>

  <div class="panel panel--3">
    <span class="front__mark" aria-hidden="true"></span>
    <h1 class="front__name">VELVET<br>CREST</h1>
    <svg class="band" viewBox="0 0 247 571" aria-hidden="true">
      <defs><linearGradient id="bandOut" x1="0" y1="1" x2="1" y2="0"><stop offset="0" stop-color="#3f8fd6"/><stop offset=".5" stop-color="#8a5cc0"/><stop offset="1" stop-color="#d6398f"/></linearGradient></defs>
      <polygon points="150,222 247,205 247,325 0,367 0,300" fill="url(#bandOut)"/>
    </svg>
    <div class="photo front__car" role="img" aria-label="Blue compact SUV, front three-quarter view"></div>
    <h2 class="services__title">SERVICES</h2>
    <ul class="services__list">
      <li>DETAILING &amp; HAND WASH</li>
      <li>POLISHING</li>
      <li>CERAMIC TREATMENT</li>
      <li>DRY ICE WASH</li>
      <li>COVERING</li>
      <li>PROTECTION FILM</li>
      <li>DETAILING BOUTIQUE</li>
    </ul>
  </div>
</section>

<section class="spread spread--inside" aria-label="Brochure inside">
  <div class="panel panel--1">
    <div class="photo wash__photo" role="img" aria-label="Microfiber wash mitt sliding over a foamy black car panel"></div>
    <div class="service wash">
      <h3 class="service__title">DETAILING &amp;<br>HAND WASH</h3>
      <ul class="bullets">
        <li>Comprehensive exterior &amp; interior care</li>
        <li>Personalisation and tailored cleaning packages</li>
        <li>Decontamination</li>
        <li>Premium products</li>
        <li>Attention to detail for a perfect finish</li>
      </ul>
    </div>
  </div>

  <div class="panel panel--2">
    <div class="service" style="left:17px;top:24px;width:150px">
      <h3 class="service__title">POLISHING</h3>
      <ul class="bullets">
        <li>Eliminates scratches, holograms</li>
        <li>Revives and protects paint</li>
        <li>Ensures lasting gloss</li>
        <li>Enhances paint life</li>
        <li>Preserves car’s value and beauty</li>
      </ul>
    </div>
    <div class="photo thumb" style="left:177px;top:40px;background:linear-gradient(180deg,#5b6e86,#2c2f36)" role="img" aria-label="Polisher with a blue pad on car paint"></div>
    <div class="rule" style="left:17px;width:206px;top:140px"></div>

    <div class="service" style="left:17px;top:151px;width:150px">
      <h3 class="service__title">CERAMIC TREATMENT</h3>
      <ul class="bullets">
        <li>Durable paint protection</li>
        <li>Water-repellent (hydrophobic) effect</li>
        <li>Easier cleaning, enhanced shine</li>
        <li>Long-term surface safeguarding</li>
        <li>Shields against environmental impacts</li>
      </ul>
    </div>
    <div class="photo thumb" style="left:177px;top:178px;background:linear-gradient(180deg,#bdbdc0,#55565a)" role="img" aria-label="Ceramic coating being applied to a wheel area"></div>
    <div class="rule" style="left:17px;width:190px;top:293px"></div>

    <div class="service" style="left:17px;top:300px;width:150px">
      <h3 class="service__title">DRY ICE WASH</h3>
      <ul class="bullets">
        <li>Innovative, waterless method</li>
        <li>Safe for all car parts</li>
        <li>Deep cleans, removes odors</li>
        <li>Allergen-free, antibacterial</li>
        <li>Gentle, effective</li>
        <li>Advanced cleaning technology</li>
      </ul>
    </div>
    <div class="photo thumb" style="left:177px;top:318px;background:linear-gradient(180deg,#e4e6e8,#3a3b3f)" role="img" aria-label="Dry ice blasting machine releasing vapour"></div>
    <div class="rule" style="left:17px;width:186px;top:427px"></div>

    <div class="service" style="left:17px;top:432px;width:152px">
      <h3 class="service__title">COVERING</h3>
      <ul class="bullets">
        <li>Personalized vehicle styling</li>
        <li>More than 150 colours available</li>
        <li>Clean cut without using a cutter</li>
        <li>High-quality, durable materials</li>
        <li>Custom designs available</li>
      </ul>
    </div>
    <div class="photo thumb" style="left:177px;top:459px;background:linear-gradient(180deg,#6a6a70,#2a2a2d 70%,#d77a2a)" role="img" aria-label="Workshop with wrap film rolls and an orange cloth"></div>
  </div>

  <div class="panel panel--3">
    <div class="service" style="left:17px;top:22px;width:160px">
      <h3 class="service__title">PROTECTION FILM</h3>
      <ul class="bullets">
        <li>Invisible, durable shield</li>
        <li>Self-healing technology</li>
        <li>10-year warranty by QR VONT</li>
      </ul>
    </div>
    <div class="photo thumb" style="left:184px;top:45px;height:87px;background:linear-gradient(180deg,#3c4048,#b9c3c8 60%,#2fb3b0)" role="img" aria-label="Protection film being applied to a car interior panel"></div>
    <div class="rule" style="left:36px;width:196px;top:141px"></div>

    <div class="service" style="left:17px;top:154px;width:165px">
      <h3 class="service__title">DETAILING BOUTIQUE</h3>
      <ul class="bullets" style="margin-top:9px">
        <li>Premium brands available</li>
        <li>Buy on site during your visit</li>
        <li>Marble Harbour, Zeb Autos, DRUP Polaro</li>
        <li>Essential for at-home car care</li>
        <li>Perfect for quick touch-ups</li>
      </ul>
    </div>

    <svg class="band" viewBox="0 0 247 571" aria-hidden="true">
      <defs><linearGradient id="bandIn" x1="0" y1="1" x2="1" y2="0"><stop offset="0" stop-color="#3f8fd6"/><stop offset=".5" stop-color="#8a5cc0"/><stop offset="1" stop-color="#d6398f"/></linearGradient></defs>
      <polygon points="0,398 247,299 247,457 0,555" fill="url(#bandIn)"/>
    </svg>
    <div class="photo inside__car" role="img" aria-label="Red sports sedan, front view"></div>
  </div>
</section>

</body>
</html>
```